Meadow Crate Co came about when a life change having to do with my health became an issue and I had to change my diet. We’re a homeschool family and learned a more simplistic way to eat and live out our day to day. We’re ready to share how we eat. Included are attachments to give a visual to the concepts in mind. The first attachment is the logo the second is basically the main idea of the company referencing to getting to the roots of nutrition and juicing. The roots design CONCEPT would be incorporated onto the bottle label. The third attachment is representing the clear stickers we’d like to have on bottles. The 4th and Last are the bottle design we’re looking to use. We’d like tall cylinder bottles.

Label must haves :
meadow crate co logo and the quote know your roots
The roots design
MeadowCrateCo.example

```html
<!DOCTYPE html>
<html lang="en">
<head>
<meta charset="utf-8">
<title>Meadow Crate Co – Juice Label</title>
<link rel="stylesheet" href="https://fonts.googleapis.com/css2?family=Chewy&family=Montserrat:wght@400;600;700;800&display=swap">
<style>
  :root {
    --canvas: #f6f6f6;
    --juice-light: #f0284a;
    --juice-mid: #d81e45;
    --juice-deep: #8e1e37;
    --ink: #ffffff;
    --logo-grey: #b5b5b5;
    --url-grey: #8a8a8a;
  }
  * { box-sizing: border-box; margin: 0; padding: 0; }
  html, body { width: 1200px; height: 1058px; overflow: hidden; }
  body {
    background: var(--canvas);
    font-family: "Montserrat", sans-serif;
    color: var(--ink);
    position: relative;
  }
  .label {
    position: absolute;
    top: 70px;
    width: 450px;
    height: 918px;
    border-radius: 18px;
    background: linear-gradient(90deg, var(--juice-mid) 0%, var(--juice-light) 30%, var(--juice-mid) 65%, var(--juice-deep) 100%);
    overflow: hidden;
  }
  .label--front { left: 110px; }
  .label--back { left: 640px; }

  /* front */
  .brand {
    position: absolute; left: 60px; top: 150px;
    display: flex; align-items: center; gap: 16px;
  }
  .brand__dot {
    width: 72px; height: 72px; border-radius: 50%;
    background: var(--logo-grey);
  }
  .brand__name {
    font-weight: 800; font-size: 30px; line-height: 1.05;
    color: var(--logo-grey); width: 200px;
  }
  .tagline {
    position: absolute; left: 0; right: 0; top: 350px;
    text-align: center; font-family: "Chewy", sans-serif;
    font-size: 62px; line-height: 0.95; letter-spacing: 1px;
  }
  .roots-art {
    position: absolute; left: 52px; top: 500px;
    width: 350px; height: 130px;
    background: radial-gradient(ellipse at 50% 20%, rgba(255,255,255,0.55), rgba(255,255,255,0.08) 60%, transparent 75%);
  }
  .facts {
    position: absolute; left: 52px; top: 680px; width: 350px;
    display: flex; gap: 12px;
  }
  .facts__info { width: 200px; }
  .facts__ingredients { font-size: 11px; font-weight: 700; line-height: 1.3; }
  .icon-row { display: flex; gap: 7px; margin-top: 9px; }
  .icon-row span {
    width: 28px; height: 28px; border-radius: 50%;
    border: 2px solid var(--ink);
  }
  .facts__divider { width: 2px; background: var(--ink); }
  .facts__type { font-weight: 800; font-size: 28px; line-height: 1; }
  .url-band {
    position: absolute; left: 45px; right: 45px;
    height: 60px; background: var(--ink);
    display: flex; align-items: center; justify-content: center;
    font-weight: 700; font-size: 27px; color: var(--url-grey);
  }
  .label--front .url-band { top: 800px; }

  /* back */
  .copy { position: absolute; left: 58px; top: 150px; width: 340px; }
  .copy h2 { font-size: 17px; font-weight: 600; margin-bottom: 12px; }
  .copy p { font-size: 12px; line-height: 1.27; margin-bottom: 22px; }
  .label--back .icon-row { margin: 0 0 14px; gap: 16px; }
  .label--back .icon-row span { width: 48px; height: 48px; }
  .ingredients-back { font-size: 14px; font-weight: 700; line-height: 1.4; }
  .closing {
    position: absolute; left: 80px; right: 80px; top: 635px;
    text-align: center; font-size: 14px; font-weight: 700; line-height: 1.4;
  }
  .label--back .url-band { top: 770px; }
</style>
</head>
<body>
  <section class="label label--front">
    <div class="brand">
      <span class="brand__dot"></span>
      <span class="brand__name">Meadow Crate Co</span>
    </div>
    <h1 class="tagline">know Your<br>Roots</h1>
    <div class="roots-art" role="img" aria-label="White line illustration of spreading plant roots"></div>
    <div class="facts">
      <div class="facts__info">
        <p class="facts__ingredients">Beetroot, Spirulina, Chlorella, Mushrooms, Pre &amp; Probiotics, Veggies, Vitamins &amp; More!</p>
        <div class="icon-row"><span></span><span></span><span></span><span></span><span></span></div>
      </div>
      <div class="facts__divider"></div>
      <p class="facts__type">Cold<br>Preseed<br>Juice</p>
    </div>
    <div class="url-band">MeadowCrateCo.example</div>
  </section>

  <section class="label label--back">
    <div class="copy">
      <h2>Lorem ipsum</h2>
      <p>Lorem ipsum dolor sit amet, consectetuer adipiscing elit, sed diam nonummy nibh euismod tincidunt ut laoreet dolore magna aliquam erat volutpat. Ut wisi enim ad minim veniam, quis nostrud exerci tation ullamcorper suscipit lobortis nisl ut aliquip ex ea commodo consequat. Duis autem vel eum iriure dolor in hendrerit in vulputate velit esse molestie consequat, vel illum dolore eu feugiat nulla facilisis.</p>
      <h2>Lorem ipsum</h2>
      <p>Lorem ipsum dolor sit amet, consectetuer adipiscing elit, sed diam nonummy nibh euismod tincidunt ut laoreet dolore magna aliquam erat volutpat. Ut wisi enim ad minim veniam, quis nostrud exerci tation ullamcorper suscipit lobortis nisl ut aliquip ex ea commodo consequat.</p>
      <div class="icon-row"><span></span><span></span><span></span><span></span><span></span></div>
      <p class="ingredients-back">Beetroot, Spirulina, Chlorella, Mushrooms, Pre &amp; Probiotics, Veggies, Vitamins &amp; More!</p>
    </div>
    <p class="closing">Lorem ipsum dolor sit amet, consectetuer adipiscing elit, sed diam nonummy nibh euismod tincidunt ut laoreet dolore</p>
    <div class="url-band">MeadowCrateCo.example</div>
  </section>
</body>
</html>
```